Bellmoor Glassware Brand Design

Logo Design Brief

Bellmoor Glassware is a startup premium drinkware company launching its first product - a premium grade 24oz Copa de Balon Gin Glass.

We are looking for branding design to produce our logo and the label for our first product; a premium 24oz Copa de Balon Gin Glass.

Design Brief for logo:

• Premium brand
• Modern, elegant and sleek design
• Not busy
• Logo does not have to include reference to drinkware

Label Design Brief:

A label design for our packaging - The packaging is tubular and will house 2 gin glasses for retail sale. The label will be stuck on the front of the tube and will need to excite people about the purchase they have just made with Bellmoor Glassware.
The label design needs to incorporate the logo and reflect our premium brand image.

• The label size is 460mm x 150mm

• Label must have modern and sleek look and must not look busy.

• The label will need to work well in both multicolour and single colour print.

• Please see attached Barcode, this will need to be incorporated into the label. Barcode will need to be 300dpi or higher and 381mm x 254mm to be scannable on the packaging.

• Please see attached pictures of the tubular packaging the label is going on to

Please also see attached 3 images of the glasses being sold - This is for reference only.

Design period has been extended for 5 Days, please ensure both a logo and corresponding packaging design is submitted. Thank you Added Wednesday, October 4, 2017

Target Market(s)

Gin Drinkers - Premium - Male and Female - All ages above 18

Industry/Entity Type

It Company

Logo Text

Bellmoor

Font styles to use
Serif
Sans Serif

Colors

Designer to choose colors to be used in the design.

Requirements
Must have
• Sleek modern design. Logo and Label must be submitted on this project.
Should not have
• Do not make this a busy logo or label

```html
<!DOCTYPE html>
<html lang="en">
<head>
<meta charset="utf-8">
<title>Bellmoor Glassware – Copa de Balon Label</title>
<link rel="stylesheet" href="https://fonts.googleapis.com/css2?family=Jost:wght@300;400&family=EB+Garamond:ital@1&display=swap">
<style>
  :root {
    --page-bg: #f0f0f0;
    --label-white: #fafafa;
    --label-shade: #eeeeee;
    --logo-grey: #6f6f6f;
    --mark-grey: #c4c4c4;
    --band-grey: #858585;
    --band-text: #ffffff;
  }
  * { margin: 0; padding: 0; box-sizing: border-box; }
  html, body {
    width: 800px;
    height: 1200px;
    overflow: hidden;
    background: var(--page-bg);
  }
  .canvas {
    position: relative;
    width: 800px;
    height: 1200px;
  }
  .label {
    position: absolute;
    left: 250px;
    top: 100px;
    width: 300px;
    height: 1000px;
    background: linear-gradient(180deg, var(--label-white) 0%, var(--label-shade) 77%);
    overflow: hidden;
  }
  .brand {
    position: absolute;
    top: 122px;
    left: 0;
    width: 100%;
    text-align: center;
    font-family: "Jost", sans-serif;
    font-weight: 300;
    color: var(--logo-grey);
  }
  .brand-name {
    display: block;
    font-size: 27px;
    letter-spacing: 4px;
    padding-left: 4px;
    line-height: 1;
  }
  .brand-line {
    display: block;
    margin-top: 8px;
    font-size: 6px;
    letter-spacing: 4.5px;
    padding-left: 4.5px;
  }
  .vertical-mark {
    position: absolute;
    left: 0;
    top: 0;
    width: 300px;
    height: 770px;
  }
  .vertical-mark text {
    font-family: "Jost", sans-serif;
    font-weight: 300;
    font-size: 58px;
    fill: var(--mark-grey);
  }
  .product-band {
    position: absolute;
    left: 0;
    top: 770px;
    width: 100%;
    height: 230px;
    background: var(--band-grey);
    color: var(--band-text);
    text-align: center;
  }
  .category {
    position: absolute;
    top: 55px;
    width: 100%;
    font-family: "Jost", sans-serif;
    font-weight: 400;
    font-size: 11px;
    letter-spacing: 2px;
  }
  .product-name {
    position: absolute;
    top: 91px;
    width: 100%;
    font-family: "EB Garamond", serif;
    font-style: italic;
    font-size: 21px;
    line-height: 29px;
  }
  .capacity {
    position: absolute;
    top: 172px;
    width: 100%;
    font-family: "Jost", sans-serif;
    font-weight: 300;
    font-size: 15px;
  }
</style>
</head>
<body>
  <main class="canvas">
    <section class="label" aria-label="Bellmoor Glassware tube label">
      <header class="brand">
        <span class="brand-name">BELLMOOR</span>
        <span class="brand-line">GLASSWARE</span>
      </header>

      <svg class="vertical-mark" viewBox="0 0 300 770" aria-hidden="true">
        <text transform="translate(171,716) rotate(-90)" textLength="498" lengthAdjust="spacing">BELLMOOR</text>
      </svg>

      <div class="product-band">
        <p class="category">PREMIUM DRINKWARE</p>
        <p class="product-name">Copa de Balon<br>Gin Glasss</p>
        <p class="capacity">24 oz</p>
      </div>
    </section>
  </main>
</body>
</html>
```